Ecommerce Website For Printing Company

Zoravquill.com are a print, design and signage company who sell flyers, business cards, posters, brochures and more to customers in the UK.

Our website is outdated and requires a new design using current web styling and mobile functionality.

We require the following pages to be designed;
- Home Page
- Price Page
- Portfolio Page
- Blog
- Content Page

Our competitors in the printing industry are www.brenticade.com, www.hallowmarsh.co.uk, quorelvane.co.uk, www.tambridok.co.uk

We require the website to give a professional image as well as be easy for customers to navigate, understand and find prices.

Target Market(s)

Businesses

Industry/Entity Type

Printing

Number of Pages Required

4 page

Font styles to use
Sans Serif

Colors
33a6d7

Requirements
Must have
• Popular products, latest news/blog, sales from portfolio, newsletter sign up, footer

```html
<!DOCTYPE html>
<html lang="en">
<head>
<meta charset="utf-8">
<title>Zoravquill.com – Print, Design &amp; Signage</title>
<link href="https://fonts.googleapis.com/css2?family=Roboto:wght@400;500;700&family=Roboto+Condensed:wght@700&family=Kaushan+Script&display=swap" rel="stylesheet">
<style>
:root{
  --brand:#33a6d7;
  --brand-dark:#1e86b5;
  --ink:#2b2b2b;
  --muted:#777;
  --line:#e2e2e2;
  --page:#f3f3f3;
  --panel:#ffffff;
  --footer:#262626;
  --footer-bottom:#1b1b1b;
  --red:#e3262b;
  --yellow:#f6c51b;
}
*{box-sizing:border-box;margin:0;padding:0}
html,body{width:1200px;height:2392px;overflow:hidden}
body{background:var(--page);font-family:"Roboto",sans-serif;color:var(--ink);font-size:13px;position:relative}
.wrap{width:1040px;margin:0 auto;position:relative}

/* top bar */
.topbar{height:22px;background:#fff;border-bottom:1px solid var(--line);font-size:11px;color:var(--muted);line-height:22px}
.topbar .wrap{display:flex;justify-content:space-between}
.topbar a{color:var(--brand);text-decoration:none}

/* header */
.header{height:100px;background:#fff}
.header .wrap{display:flex;align-items:center;justify-content:space-between;height:100px}
.logo{display:flex;align-items:center;gap:10px}
.logo-name{font-family:"Roboto Condensed",sans-serif;font-weight:700;font-size:38px;color:var(--brand);letter-spacing:-.5px}
.logo-mark{width:14px;height:14px;background:var(--brand)}
.search{width:250px;height:30px;border:1px solid #ccc;display:flex;align-items:center;justify-content:space-between;padding:0 8px;font-size:11px;color:#999}
.cart{display:flex;align-items:center;gap:10px}
.cart-icon{width:40px;height:40px;border-radius:50%;background:var(--brand);display:flex;align-items:center;justify-content:center}
.cart-text b{display:block;font-size:12px;text-transform:uppercase}
.cart-text span{font-size:11px;color:var(--muted)}

/* nav */
.nav{height:34px;background:var(--brand)}
.nav .wrap{display:flex;justify-content:space-between;align-items:center;height:34px}
.nav ul{display:flex;list-style:none}
.nav li{color:#fff;font-family:"Roboto Condensed",sans-serif;font-size:13px;padding:0 18px;line-height:34px}
.nav li:first-child{padding-left:0}
.nav .call{color:#fff;font-size:11px}
.nav .call b{font-family:"Roboto Condensed",sans-serif;font-size:20px;margin-left:6px;vertical-align:-2px}

/* hero */
.hero{height:564px;padding-top:24px}
.hero-box{height:496px;background:linear-gradient(180deg,#e9e9e9,#d6d6d6);border:1px solid var(--line);position:relative;overflow:hidden}
.hero-copy{position:absolute;left:370px;top:70px}
.hero-title{font-family:"Roboto",sans-serif;font-weight:700;font-size:46px;color:var(--ink)}
.hero-sub{font-family:"Kaushan Script",cursive;font-size:28px;color:var(--red);margin:6px 0 0 40px}
.hero-art{position:absolute;left:560px;top:160px;width:460px;height:300px;background:linear-gradient(135deg,#f6f6f6,#c8dff0 50%,#e8b9b9);border-radius:4px}
.hero-art-top{position:absolute;left:400px;top:20px;width:180px;height:150px;background:linear-gradient(135deg,#e0433f,#f2c6c3);border-radius:4px}
.btn-shop{position:absolute;left:50px;top:330px;background:#222;color:#fff;font-family:"Roboto Condensed",sans-serif;font-size:18px;padding:14px 26px;border:2px solid #fff;outline:2px solid #222}
.price-badge{position:absolute;left:500px;top:330px;width:140px;height:140px;border-radius:50%;background:var(--red);border:4px solid #fff;color:#fff;text-align:center;padding-top:26px}
.price-badge span{font-size:13px;font-weight:700;display:block}
.price-badge b{font-size:48px;font-family:"Roboto Condensed",sans-serif;line-height:1}
.dots{display:flex;gap:6px;margin-top:12px}
.dots i{width:9px;height:9px;border-radius:50%;background:#bbb}
.dots i:first-child{background:#333}

/* panels */
.panel{background:var(--panel);border:1px solid var(--line)}
.section-tab{display:inline-block;font-family:"Roboto Condensed",sans-serif;font-size:18px;padding:10px 20px;background:#fff;border-bottom:3px solid var(--brand)}
.arrows{position:absolute;right:14px;top:12px;display:flex;gap:6px}
.arrows i{width:18px;height:18px;border-radius:50%;background:#ccc}

.products{height:480px}
.products .panel{height:456px;position:relative}
.product-row{display:flex;gap:28px;padding:24px 24px 0}
.product{width:227px}
.product-img{height:170px;border:1px solid var(--line)}
.product h3{font-size:15px;font-weight:500;margin:14px 0 6px}
.product p{font-size:11px;color:var(--muted);line-height:1.5;height:50px}
.btn-learn{display:inline-block;background:#333;color:#fff;font-size:10px;font-weight:700;padding:7px 12px;margin-top:6px}

/* blog & news */
.blognews{height:500px;display:flex;gap:30px;padding-top:10px}
.blog{width:700px}
.news{width:310px}
.col-title{font-family:"Roboto Condensed",sans-serif;font-size:18px;padding-bottom:10px;border-bottom:1px solid var(--line);margin-bottom:16px}
.blog-grid{display:flex;gap:30px}
.blog-post{width:335px}
.blog-post h4{font-size:15px;font-weight:500;line-height:1.3}
.meta{font-size:10px;color:var(--muted);margin:6px 0 12px}
.blog-body{display:flex;gap:12px}
.blog-thumb{width:90px;height:90px;flex:none}
.blog-body p{font-size:11px;color:var(--muted);line-height:1.55}
.more{font-size:11px;color:var(--red);font-weight:700;margin-top:10px;display:block}
.blog-post+.blog-post{}
.news-item{display:flex;gap:12px;margin-bottom:22px}
.news-thumb{width:70px;height:70px;flex:none}
.news-item h5{font-size:12px;font-weight:500;line-height:1.35}
.news-item .meta{margin:3px 0}

/* portfolio */
.portfolio{height:310px}
.portfolio .panel{height:290px;position:relative;text-align:center}
.portfolio .section-tab{margin-top:-1px}
.port-row{display:flex;gap:26px;justify-content:center;padding-top:26px}
.port-item{width:200px;height:190px;border:1px solid var(--line)}
.side-arrow{position:absolute;top:135px;width:24px;height:24px;border-radius:50%;background:#ccc}

/* newsletter */
.newsletter{height:60px;background:var(--brand)}
.newsletter .wrap{display:flex;align-items:center;height:60px;gap:20px}
.newsletter h3{color:#fff;font-family:"Roboto Condensed",sans-serif;font-size:15px;line-height:1.15;width:330px}
.news-input{width:300px;height:30px;background:#fff}
.btn-sub{background:var(--yellow);color:#222;font-family:"Roboto Condensed",sans-serif;font-size:14px;padding:7px 22px}

/* footer */
.footer{height:255px;background:var(--footer);color:#bbb}
.footer .wrap{display:flex;padding-top:28px}
.fcol{width:260px}
.fcol h6{color:#fff;font-family:"Roboto Condensed",sans-serif;font-size:13px;margin-bottom:12px}
.fcol li{list-style:none;font-size:11px;line-height:2}
.contact{display:flex;gap:10px;align-items:flex-start;margin-bottom:16px}
.contact-icon{width:30px;height:30px;border-radius:50%;background:#444;display:flex;align-items:center;justify-content:center;flex:none}
.contact b{color:#fff;font-size:12px;display:block}
.contact span{font-size:11px}
.footer-bottom{height:63px;background:var(--footer-bottom)}
.footer-bottom .wrap{display:flex;align-items:center;height:63px;gap:20px;color:#999;font-size:11px}
.social{display:flex;gap:6px}
.social i{width:20px;height:20px;border-radius:50%;background:#555}
.cards{margin-left:auto;display:flex;gap:5px}
.cards i{width:34px;height:22px;background:#ddd;border-radius:2px}
</style>
</head>
<body>

<div class="topbar"><div class="wrap">
  <span>Welcome to Zoravquill.com: <a>Sign in</a> or <a>Register</a></span>
  <span>My Account | Check Out | Wishlist | Live Chat</span>
</div></div>

<header class="header"><div class="wrap">
  <div class="logo"><span class="logo-mark"></span><span class="logo-name">Zoravquill.com</span></div>
  <div class="search"><span>Enter keywords...</span>
    <svg width="14" height="14" viewBox="0 0 14 14"><circle cx="6" cy="6" r="4.5" fill="none" stroke="#888" stroke-width="1.6"/><line x1="9.3" y1="9.3" x2="13" y2="13" stroke="#888" stroke-width="1.6"/></svg>
  </div>
  <div class="cart">
    <div class="cart-icon"><svg width="20" height="18" viewBox="0 0 20 18"><path d="M1 2h3l2 10h10l2-7H5" fill="none" stroke="#fff" stroke-width="1.8"/><circle cx="8" cy="15.5" r="1.6" fill="#fff"/><circle cx="15" cy="15.5" r="1.6" fill="#fff"/></svg></div>
    <div class="cart-text"><b>Shopping Cart</b><span>0 items - £0.00</span></div>
  </div>
</div></header>

<nav class="nav"><div class="wrap">
  <ul><li>HOME</li><li>ABOUT</li><li>PRODUCTS</li><li>PRICE</li><li>PORTFOLIO</li><li>BLOG</li><li>CONTACT</li></ul>
  <span class="call">Need advice? Call us<b>01632 960 418</b></span>
</div></nav>

<section class="hero"><div class="wrap">
  <div class="hero-box">
    <div class="hero-art-top" role="img" aria-label="Photo of printed greeting cards"></div>
    <div class="hero-copy">
      <div class="hero-title">Brochure Printing</div>
      <div class="hero-sub">Better Printing, Better Services!</div>
    </div>
    <div class="hero-art" role="img" aria-label="Photo of folded brochures and flyers"></div>
    <div class="btn-shop">SHOP NOW</div>
    <div class="price-badge"><span>FROM JUST</span><b>£99</b></div>
  </div>
  <div class="dots"><i></i><i></i><i></i><i></i><i></i></div>
</div></section>

<section class="products"><div class="wrap"><div class="panel">
  <div class="section-tab">POPULAR PRODUCTS</div>
  <div class="arrows"><i></i><i></i></div>
  <div class="product-row">
    <div class="product"><div class="product-img" role="img" aria-label="Photo of business card stacks" style="background:linear-gradient(135deg,#eef6fa,#3f8fb0 60%,#d84b4b)"></div><h3>Business Cards</h3><p>Lorem ipsum dolor sit amet, consectetur adipiscing elit, sed do eiusmod.</p><span class="btn-learn">LEARN MORE</span></div>
    <div class="product"><div class="product-img" role="img" aria-label="Photo of party posters" style="background:linear-gradient(135deg,#f4f4f4,#3a2e8c 55%,#1d8bd1)"></div><h3>Posters</h3><p>Lorem ipsum dolor sit amet, consectetur adipiscing elit, sed do eiusmod.</p><span class="btn-learn">LEARN MORE</span></div>
    <div class="product"><div class="product-img" role="img" aria-label="Photo of tri-fold brochures" style="background:linear-gradient(135deg,#f7f7f7,#2c8fbf 55%,#f0f0f0)"></div><h3>Brochures</h3><p>Lorem ipsum dolor sit amet, consectetur adipiscing elit, sed do eiusmod.</p><span class="btn-learn">LEARN MORE</span></div>
    <div class="product"><div class="product-img" role="img" aria-label="Photo of flyers" style="background:linear-gradient(135deg,#f5f5f5,#1e9fb8 55%,#f2d04a)"></div><h3>Flyers</h3><p>Lorem ipsum dolor sit amet, consectetur adipiscing elit, sed do eiusmod.</p><span class="btn-learn">LEARN MORE</span></div>
  </div>
</div></div></section>

<section class="wrap blognews">
  <div class="blog">
    <div class="col-title">LATEST BLOG</div>
    <div class="blog-grid">
      <article class="blog-post">
        <h4>Lorem ipsum dolor sit amet consectetur adipiscing elit</h4>
        <div class="meta">26 Nov, 2015 | 24 Comments</div>
        <div class="blog-body"><div class="blog-thumb" role="img" aria-label="Photo of printed cards" style="background:linear-gradient(135deg,#e9e9e9,#c9417a)"></div>
          <p>Consectetur adipiscing elit, sed do eiusmod tempor incididunt ut labore et dolore magna aliqua. Ut enim ad minim veniam, quis nostrud exercitation ullamco laboris nisi ut aliquip ex ea commodo consequat duis aute irure.</p></div>
        <span class="more">More →</span>
      </article>
      <article class="blog-post">
        <h4>Lorem ipsum dolor sit amet consectetur adipiscing elit</h4>
        <div class="meta">26 Nov, 2015 | 24 Comments</div>
        <div class="blog-body"><div class="blog-thumb" role="img" aria-label="Photo of brochures" style="background:linear-gradient(135deg,#e9e9e9,#3a8fc0)"></div>
          <p>Consectetur adipiscing elit, sed do eiusmod tempor incididunt ut labore et dolore magna aliqua. Ut enim ad minim veniam, quis nostrud exercitation ullamco laboris nisi ut aliquip ex ea commodo consequat duis aute irure.</p></div>
        <span class="more">More →</span>
      </article>
    </div>
  </div>
  <div class="news">
    <div class="col-title">LATEST NEWS</div>
    <div class="news-item"><div class="news-thumb" role="img" aria-label="Photo of flyer print" style="background:linear-gradient(135deg,#f2d04a,#e4507a)"></div><div><h5>Lorem ipsum dolor sit amet consectetur adipiscing elit</h5><div class="meta">26 Nov, 2015</div><span class="more">More →</span></div></div>
    <div class="news-item"><div class="news-thumb" role="img" aria-label="Photo of party poster" style="background:linear-gradient(135deg,#3a2e8c,#1d8bd1)"></div><div><h5>Lorem ipsum dolor sit amet consectetur adipiscing elit</h5><div class="meta">26 Nov, 2015</div><span class="more">More →</span></div></div>
    <div class="news-item"><div class="news-thumb" role="img" aria-label="Photo of greeting card" style="background:linear-gradient(135deg,#e0433f,#f2c6c3)"></div><div><h5>Lorem ipsum dolor sit amet consectetur adipiscing elit</h5><div class="meta">26 Nov, 2015</div><span class="more">More →</span></div></div>
  </div>
</section>

<section class="portfolio"><div class="wrap"><div class="panel">
  <div class="section-tab">SALES FROM PORTFOLIO</div>
  <span class="side-arrow" style="left:16px"></span>
  <div class="port-row">
    <div class="port-item" role="img" aria-label="Sale flyer design" style="background:linear-gradient(135deg,#f2d04a,#e23d6e)"></div>
    <div class="port-item" role="img" aria-label="Folded brochure design" style="background:linear-gradient(135deg,#f5f5f5,#2c8fbf)"></div>
    <div class="port-item" role="img" aria-label="Menu leaflet design" style="background:linear-gradient(135deg,#5a2b1c,#c28a4a)"></div>
    <div class="port-item" role="img" aria-label="Corporate brochure design" style="background:linear-gradient(135deg,#eeeeee,#d24a4a 60%,#3a6fb0)"></div>
  </div>
  <span class="side-arrow" style="right:16px"></span>
</div></div></section>

<section class="newsletter"><div class="wrap">
  <h3>SUBSCRIBE TO OUR NEWSLETTER<br>&amp; GET THE BEST DEALS FIRST!</h3>
  <div class="news-input"></div>
  <span class="btn-sub">SUBSCRIBE</span>
</div></section>

<footer>
  <div class="footer"><div class="wrap">
    <div class="fcol"><h6>INFORMATION</h6><ul><li>About Us</li><li>Delivery Information</li><li>Privacy Policy</li><li>Terms &amp; Conditions</li><li>Site Map</li><li>Returns Policy</li><li>Contact Us</li></ul></div>
    <div class="fcol"><h6>WHY BUY FROM US</h6><ul><li>Quality Print</li><li>Fast Turnaround</li><li>Free Delivery</li><li>Secure Payment</li><li>Price Match</li></ul></div>
    <div class="fcol"><h6>MY ACCOUNT</h6><ul><li>Sign In</li><li>View Cart</li><li>My Wishlist</li><li>Track My Order</li><li>Help</li></ul></div>
    <div class="fcol">
      <div class="contact"><span class="contact-icon"><svg width="14" height="10" viewBox="0 0 14 10"><rect x=".5" y=".5" width="13" height="9" fill="none" stroke="#fff"/><path d="M.5 .5 7 6l6.5-5.5" fill="none" stroke="#fff"/></svg></span><div><b>EMAIL US</b><span>hello@zoravquill.com</span></div></div>
      <div class="contact"><span class="contact-icon"><svg width="12" height="14" viewBox="0 0 12 14"><path d="M2 1l3 3-1.5 2a8 8 0 0 0 3.5 3.5L9 8l3 3-2 2C5 13 0 7 0 3z" fill="#fff"/></svg></span><div><b>CALL US</b><span>01632 960 418</span></div></div>
    </div>
  </div></div>
  <div class="footer-bottom"><div class="wrap">
    <div class="social"><i></i><i></i><i></i><i></i></div>
    <span>© 2016 Zoravquill.com. All rights reserved.</span>
    <div class="cards"><i></i><i></i><i></i><i></i><i></i></div>
  </div></div>
</footer>

</body>
</html>
```